Comet Speakers™ – Water Resistant Bluetooth Speakers

Looking for someone who is very experienced with retail product packaging.
We currently have a blank retail box with product window area and we need a design created to print on that box.
The design will need to be crisp, clean and appealing to consumers as well as have all of the proper retail wording, requirements etc.
The product is a bluetooth speaker/speakerphone that goes anywhere, even the shower!
We need this created asap.
Updates

Reason: We have quite a few really good designs, we want to give everyone a chance to work with our team to get text and layouts updated how we want them and then we will make a final decision.

Target Market(s)

Consumer Electronics Shoppers

Industry/Entity Type

Retail

Requirements
Must have
• Design must stand out to consumers and clearly display what makes this product unique but remain clean and simple, think Tessary packaging.
Printed areas must include all 4 sides and top of box.
UPC area on the back of box.
See http://www.halvardgoods.com/product/comet-speakers-water-resistant-bluetooth-speakers/ for product details and descriptions.
Nice to have
• No need for a logo, can just be font based, if you make a logo great, but not needed.

```html
<!DOCTYPE html>
<html lang="en">
<head>
<meta charset="utf-8">
<title>Comet Speakers – Retail Box Dieline</title>
<link rel="stylesheet" href="https://fonts.googleapis.com/css2?family=Arimo:wght@400;700&family=Questrial&display=swap">
<style>
  :root {
    --brand-blue: #1279c2;
    --banner-blue: #1b9ad8;
    --aqua: #4cc8f0;
    --aqua-pale: #d6eefa;
    --ink: #1e1e1e;
    --dieline: #555555;
    --window-grey: #4f4f4f;
    --paper: #ffffff;
  }
  * { margin: 0; padding: 0; box-sizing: border-box; }
  html, body { width: 1200px; height: 1000px; overflow: hidden; background: var(--paper); }
  .dieline-sheet { position: relative; width: 1200px; height: 1000px; font-family: "Arimo", Arial, sans-serif; color: var(--ink); }
  .dieline-sheet > * { position: absolute; }
  .cut-lines { left: 0; top: 0; }

  .splash { background: radial-gradient(ellipse at 80% 40%, #ffffff 0%, var(--aqua-pale) 35%, #9fd3ef 55%, rgba(255,255,255,0) 75%); }
  .splash--top { left: 440px; top: 173px; width: 137px; height: 215px; }
  .splash--side { left: 15px; top: 439px; width: 215px; height: 125px; background: radial-gradient(ellipse at 30% 20%, #ffffff 0%, var(--aqua-pale) 35%, #9fd3ef 55%, rgba(255,255,255,0) 75%); }
  .splash--front { left: 320px; top: 439px; width: 257px; height: 231px; background: radial-gradient(ellipse at 55% 50%, #ffffff 0%, var(--aqua-pale) 40%, #a7d7f1 58%, rgba(255,255,255,0) 76%); }
  .splash--back { left: 945px; top: 545px; width: 212px; height: 125px; background: radial-gradient(ellipse at 80% 75%, #ffffff 0%, var(--aqua-pale) 35%, #9fd3ef 55%, rgba(255,255,255,0) 75%); }

  .brand-lockup { left: 278px; top: 300px; display: flex; align-items: center; gap: 7px; white-space: nowrap; }
  .brand-dot { width: 22px; height: 22px; border-radius: 50%; background: var(--brand-blue); flex: none; }
  .brand-name { font-family: "Questrial", Arial, sans-serif; font-size: 32px; color: var(--brand-blue); line-height: 1; }
  .brand-tagline { font-family: "Questrial", Arial, sans-serif; font-size: 12.5px; color: var(--brand-blue); line-height: 14px; margin-left: 3px; }

  .front-name { left: 280px; top: 452px; width: 50px; font-family: "Questrial", Arial, sans-serif; font-size: 36px; color: var(--brand-blue); line-height: 27px; text-align: center; display: flex; flex-direction: column; }
  .front-name span { display: block; height: 27px; }
  .front-banner { left: 247px; top: 610px; width: 121px; height: 16px; background: var(--banner-blue); color: #fff; font-size: 10.5px; line-height: 16px; padding-left: 22px; white-space: nowrap; }
  .front-banner .mark { position: absolute; left: 10px; top: 4px; width: 8px; height: 8px; border-radius: 50%; background: #fff; }
  .front-subtitle { left: 253px; top: 631px; width: 100px; text-align: center; font-family: "Questrial", Arial, sans-serif; font-size: 12.5px; line-height: 14px; color: var(--brand-blue); }

  .product-window { left: 369px; top: 477px; width: 173px; height: 159px; border-radius: 10px; background: var(--window-grey); border: 1px solid #333; color: #fff; font-size: 26px; display: flex; align-items: center; justify-content: center; }

  .spec-panel { left: 579px; top: 439px; width: 231px; height: 231px; background: linear-gradient(90deg, var(--aqua) 0%, #a8def5 45%, #ffffff 100%); }
  .spec-list { left: 601px; top: 453px; width: 180px; font-size: 9px; line-height: 11.5px; }
  .spec-list h3, .feature-list h3 { font-size: 9px; font-weight: 700; }
  .spec-list ul, .feature-list ul { list-style: none; }
  .spec-list li, .feature-list li { padding-left: 8px; text-indent: -7px; }
  .spec-list li::before, .feature-list li::before { content: "• "; }

  .back-intro { left: 831px; top: 446px; width: 296px; font-size: 10.5px; line-height: 12.4px; }
  .feature-list { left: 833px; top: 505px; width: 262px; font-size: 9px; line-height: 11.3px; }
  .upc-area { left: 838px; top: 628px; width: 89px; height: 39px; border: 1.5px solid #222; font-size: 25px; font-weight: 700; display: flex; align-items: center; justify-content: center; }
</style>
</head>
<body>
<main class="dieline-sheet">
  <svg class="cut-lines" width="1200" height="1000" viewBox="0 0 1200 1000" aria-hidden="true">
    <g fill="none" stroke="var(--dieline)" stroke-width="1">
      <path d="M247 438 V185 Q247 172 262 172 H565 Q578 172 578 185 V438"/>
      <path d="M235 438 V336 H55 L14 415 V671"/>
      <path d="M590 438 V336 H770 L810 415 V438"/>
      <path d="M14 671 V690 L134 746 V797 H247 V671"/>
      <path d="M247 671 L330 785 V823 H497 V785 L578 671"/>
      <path d="M578 671 V797 H690 V746 L810 690 V671"/>
      <path d="M810 671 V820 H893 V787 H1058 V820 H1142 V671"/>
      <path d="M810 438 H1142 L1185 448 V662 L1142 671"/>
      <path d="M14 438 H247"/>
    </g>
    <g fill="none" stroke="#8a8a8a" stroke-width="1" stroke-dasharray="3 3">
      <path d="M247 207 H578"/>
      <path d="M14 438 H810"/>
      <path d="M14 671 H1142"/>
      <path d="M247 438 V671 M578 438 V671 M810 438 V671 M1142 438 V671"/>
    </g>
  </svg>

  <div class="splash splash--top" role="img" aria-label="Water splash illustration"></div>
  <div class="splash splash--side" role="img" aria-label="Water splash illustration"></div>
  <div class="splash splash--front" role="img" aria-label="Water splash ring around the product window"></div>
  <div class="splash splash--back" role="img" aria-label="Water splash illustration"></div>

  <div class="brand-lockup">
    <span class="brand-dot"></span>
    <span class="brand-name">COMET</span>
    <span class="brand-tagline">WATER RESISTANT<br>BLUETOOTH SPEAKER</span>
  </div>

  <div class="front-name"><span>C</span><span>O</span><span>M</span><span>E</span><span>T</span></div>
  <div class="front-banner"><span class="mark"></span>WATER RESISTANT</div>
  <div class="front-subtitle">BLUETOOTH<br>SPEAKER</div>
  <div class="product-window">Window</div>

  <div class="spec-panel"></div>
  <section class="spec-list">
    <h3>Specifications:</h3>
    <ul>
      <li>Super portable—only 2.25 inches tall</li>
      <li>Up to 6 hours talk time</li>
      <li>33 foot range</li>
      <li>Rechargeable battery</li>
      <li>Includes a USB cable for charging your Comet Speaker</li>
    </ul>
  </section>

  <p class="back-intro">Meet Comet, the brave little speaker that isn’t afraid to go where other speakers won’t because he’s water resistant! Stream music and take calls from the wireless speaker that sticks to anything!</p>
  <section class="feature-list">
    <h3>Features:</h3>
    <ul>
      <li>Compatible with smartphones, tablets, laptops, MP3 players or any Bluetooth-enabled device</li>
      <li>Streams music</li>
      <li>Take speakerphone calls with Comet’s built-in microphone</li>
      <li>Skip music tracks, adjust the volume and answer phone calls from anywhere</li>
      <li>Built-in suction cup sticks to almost any surface: Walls &amp; tables, refrigerators, phones, car dashes, showers and more!</li>
    </ul>
  </section>
  <div class="upc-area">UPC</div>
</main>
</body>
</html>
```